Mortgage Company ready to make a statement!

We have a basic logo that I am fairly happy with ... but it could use a little bit of tweaking before we order the sign for our building. We also want some knock-your-socks-off business cards.
Problem: Inside of our Mortgage Office (Brindle Oak Mortgage Group), we are going to have a coffee lounge (Mapleburr Cafe) for Realtors to use instead of the local Quillmont to meet with homebuyers. The office and coffee lounge are in an industrial building and is decorated with cozy overstuffed chairs, a hodge podge of interesting lamps and furniture, and goal is to make it as inviting as possible. However, we are a financial institution... so we need to keep it pretty clean as well.
One of my favorite marketing ideas is to cut a house key for everyone who buys a home using us with a key that matches our logo. There's only one key shape that works really well, so that needs to match the logo in order for the idea to work. I'll attach an image of the key blank.... although the way the key hole cut out looks terrible, so I was thinking of having them just do a thin outline instead.
Would like a similar, matching logo for the Mapleburr Cafe... but possibly something that would be a little less formal and would be cute on a coffee mug- nothing stuffy.
AND, we're opening a home inspection company as well, and we would like that logo and branding to match. The home inspection company is "Brindle Oak Home Inspections"
We were thinking that for the home inspection company , we could use a magnifying glass shape inside of the house shape for the logo, use a keyhole shape inside of the same house for the mortgage company, and use a coffee cup inside of the house shape for Mapleburr Cafe.
Just getting stuck and need to help. I designed the attached logo myself, and that is what we are currently using. Designers at local printing companies have failed to impress us.
The mortgage industry has a lot of numbers and logos, etc that they require us to put on our business cards... so it's hard to keep them looking clean.
HELP! HELP! :)

```html
<!DOCTYPE html>
<html lang="en">
<head>
<meta charset="UTF-8">
<title>Brindle Oak Mortgage Group – Business Card</title>
<link href="https://fonts.googleapis.com/css2?family=Montserrat:wght@300;400;700&display=swap" rel="stylesheet">
<style>
  :root {
    --backdrop: #2e2f31;
    --card-blue: #236686;
    --card-edge: #1d5672;
    --ink-white: #ffffff;
  }
  * { margin: 0; padding: 0; box-sizing: border-box; }
  html, body {
    width: 1200px; height: 900px; overflow: hidden;
    background: var(--backdrop);
    font-family: "Montserrat", sans-serif;
    color: var(--ink-white);
  }
  .sheet {
    width: 1200px; height: 900px;
    display: flex; flex-direction: column;
    align-items: center; justify-content: center; gap: 60px;
  }
  .card {
    width: 560px; height: 320px;
    background: var(--card-blue);
    border-radius: 22px;
    box-shadow: 0 2px 0 var(--card-edge), 0 18px 40px rgba(0,0,0,.45);
    position: relative;
    overflow: hidden;
  }
  /* Front */
  .card--front { display: flex; align-items: center; justify-content: center; }
  .brand { display: flex; align-items: center; gap: 22px; }
  .brand__square { width: 44px; height: 44px; background: var(--ink-white); flex: none; }
  .brand__name { font-weight: 300; line-height: 1.05; letter-spacing: 1px; }
  .brand__main { display: block; font-size: 48px; text-transform: uppercase; }
  .brand__sub { display: block; font-size: 26px; margin-top: 4px; }

  /* Back */
  .identity {
    position: absolute; left: 50px; top: 110px; width: 190px; text-align: right;
  }
  .identity__name { font-weight: 700; font-size: 22px; letter-spacing: 1.5px; text-transform: uppercase; white-space: nowrap; }
  .identity__role { font-weight: 700; font-size: 16px; letter-spacing: 1px; margin-top: 4px; }
  .divider {
    position: absolute; left: 258px; top: 108px; width: 2px; height: 68px; background: var(--ink-white);
  }
  .contact { position: absolute; left: 278px; top: 110px; list-style: none; }
  .contact li {
    display: flex; align-items: center; gap: 10px;
    font-size: 14px; font-weight: 400; letter-spacing: .5px; line-height: 22px;
    white-space: nowrap;
  }
  .contact svg { width: 14px; height: 14px; flex: none; }
  .address {
    position: absolute; left: 50px; bottom: 60px;
    font-size: 16px; letter-spacing: 1.5px; font-weight: 400;
  }
</style>
</head>
<body>
<main class="sheet">
  <section class="card card--front" aria-label="Card front">
    <div class="brand">
      <span class="brand__square"></span>
      <p class="brand__name">
        <span class="brand__main">Brindle Oak</span>
        <span class="brand__sub">Mortgage Group</span>
      </p>
    </div>
  </section>

  <section class="card card--back" aria-label="Card back">
    <div class="identity">
      <p class="identity__name">Corin Vashti</p>
      <p class="identity__role">CEO</p>
    </div>
    <span class="divider"></span>
    <ul class="contact">
      <li>
        <svg viewBox="0 0 14 14" aria-hidden="true"><rect x="4" y="1" width="6" height="12" rx="1" fill="none" stroke="#fff" stroke-width="1.3"/><line x1="6" y1="11" x2="8" y2="11" stroke="#fff" stroke-width="1.2"/></svg>
        000-555-0142
      </li>
      <li>
        <svg viewBox="0 0 14 14" aria-hidden="true"><rect x="4" y="1" width="6" height="4" fill="#fff"/><rect x="1" y="5" width="12" height="5" rx="1" fill="#fff"/><rect x="4" y="9" width="6" height="4" fill="#fff"/></svg>
        000-555-0142
      </li>
      <li>
        <svg viewBox="0 0 14 14" aria-hidden="true"><rect x="1" y="3" width="12" height="8" fill="#fff"/><polyline points="1,3 7,8 13,3" fill="none" stroke="#236686" stroke-width="1.2"/></svg>
        corin@brindleoak.example
      </li>
    </ul>
    <p class="address">Tallow Court Centre Sydney Melbourne</p>
  </section>
</main>
</body>
</html>
```